Harbinger Noble Alloys Works Business Cards

We are wanting to have a new business card designed for our company as we go to a convention. We want to balance business/Modern with elegance and beauty. Our company sells highend jewelry pieces. We want to utilize the colors of Black and Gold and have gold foiled fonts to be physically printed on the business cards.
We also would like to have space to write notes on the back side of the business card. When we meet people at jewelry conventions we would like to write notes if possible.
Here are websites and designs that we like the look and feel of these companies and you can use these as design ideas.
https://www.lorvanne.com
https://www.bellquist.com/en-us/home
Here is our company website link
www.harbingernaw.com
I also up loaded two versions of our logo.
- Update 4.26.22
I have uploaded photos of a business card we like. this card has raised embossed letters that you can feel. the raise letters are like a plastic but we don't need to use that...I uploaded to show you that we like the experience of the client feeling the characters of the logo. we also would like to have the material as a satin or some material very soft.
- Maybe we can get designs with beautiful gold foiling and raised characters and logos. we like simplicity...not busy but an elegant design. We need to write notes and would like a section where we can write notes. but we want an elegant style and the client has an experience with the feel of the card when they touch the card.
Colors
- Main colors Black & Gold
- white or light colors for small notes section.
Specialty ideals and things we would like to see based on your design styles.
- raised fonts
- raised logos
- gold foiling
- satin/soft finish on the card material.
we are wanting to design a business card that looks elegant and clean. When the client is handed the business card we want them to physically experience the business card as well by touching the raised logos or fonts and the base material is soft satin. I hope this helps with further designs.
thank you all
We uploaded a new contact layout that we have designed in our office. we would like to see how this would look on your designs.
thank you
I just finished uploading the Contact Layout. the colors are just examples. please use this layout as an idea and use colors based on the feed back we have given each of you personally.
Contact Information for Business Card
we need an area to write notes, we would like to have our logos or the diamond of our logo or the business card to have embossed sections to the business card so when the customer touches the card they can feel the logo. we would also like sections of our business card to have gold foiling. we would also like to use a satin soft paper with our card. when the client touches the card its super soft and high quality
Requirements
Must have
- we would like to have our logos or the diamond of our logo or the business card to have embossed sections to the business card so when the customer touches the card they can feel the logo. we would also like sections of our business card to have gold foiling. we would also like to use a satin soft paper with our card. when the client touches the card its super soft and high quality
Nice to have
- we would like to have our logos or the diamond of our logo or the business card to have embossed sections to the business card so when the customer touches the card they can feel the logo. we would also like sections of our business card to have gold foiling.

```html
<!DOCTYPE html>
<html lang="en">
<head>
<meta charset="utf-8">
<title>Harbinger Noble Alloys Works – Business Card</title>
<link href="https://fonts.googleapis.com/css2?family=Cinzel:wght@500&family=Open+Sans:ital,wght@0,400;0,700;1,400&display=swap" rel="stylesheet">
<style>
  :root {
    --stage: #1c1c1c;
    --card-black: #111111;
    --emboss: #3a3a3a;
    --gold: #c9a063;
    --gold-dark: #8a6a3a;
    --ink-light: #f2f2f2;
    --notes-paper: #ffffff;
    --notes-line: #d8d8d8;
  }
  * { box-sizing: border-box; margin: 0; padding: 0; }
  html, body { width: 1200px; height: 900px; overflow: hidden; }
  body {
    background: var(--stage);
    display: flex;
    flex-direction: column;
    align-items: center;
    justify-content: center;
    gap: 60px;
    font-family: "Open Sans", sans-serif;
  }
  .card {
    width: 560px;
    height: 320px;
    background: var(--card-black);
    box-shadow: 0 18px 40px rgba(0,0,0,.55);
    position: relative;
    overflow: hidden;
  }
  /* Front */
  .card-front {
    display: flex;
    align-items: center;
    justify-content: center;
  }
  .brand-name {
    font-family: "Cinzel", serif;
    font-weight: 500;
    font-size: 34px;
    letter-spacing: 1px;
    color: var(--emboss);
    text-align: center;
    line-height: 1.2;
  }
  /* Back */
  .card-back { display: flex; }
  .contact-panel {
    width: 56%;
    padding: 92px 0 0 44px;
    color: var(--ink-light);
  }
  .person-name {
    font-weight: 700;
    font-size: 22px;
    letter-spacing: .5px;
    text-transform: uppercase;
    background: linear-gradient(90deg, var(--gold-dark), var(--gold) 45%, #e6c792 60%, var(--gold-dark));
    -webkit-background-clip: text;
    background-clip: text;
    color: transparent;
  }
  .person-title { font-size: 14px; font-style: italic; margin-bottom: 16px; }
  .address { font-size: 13px; line-height: 1.45; margin-bottom: 8px; }
  .contact-list { list-style: none; font-size: 13px; line-height: 1.55; }
  .contact-list li { display: flex; align-items: center; gap: 8px; }
  .contact-icon { width: 12px; height: 12px; flex: none; }
  .notes-panel {
    flex: 1;
    background: var(--notes-paper);
    display: flex;
    justify-content: space-evenly;
    padding: 36px 40px;
  }
  .notes-line { width: 1px; background: var(--notes-line); }
</style>
</head>
<body>

  <section class="card card-front" aria-label="Business card front">
    <h1 class="brand-name">Harbinger Noble<br>Alloys Works</h1>
  </section>

  <section class="card card-back" aria-label="Business card back">
    <div class="contact-panel">
      <p class="person-name">Dorian Velasque</p>
      <p class="person-title">President</p>
      <p class="address">742 Marlow Crest Rd<br>Ashford, OR 97388</p>
      <ul class="contact-list">
        <li>
          <svg class="contact-icon" viewBox="0 0 12 12" aria-hidden="true"><circle cx="6" cy="6" r="6" fill="var(--gold)"/><path d="M4 3.2l1.2 1.4-.6.8c.4.8 1 1.4 1.8 1.8l.8-.6 1.4 1.2-.8 1c-2.2-.3-4-2.1-4.3-4.3z" fill="var(--card-black)"/></svg>
          (555) 218-4730
        </li>
        <li>
          <svg class="contact-icon" viewBox="0 0 12 12" aria-hidden="true"><rect x="1" y="3" width="10" height="6.5" fill="var(--gold)"/><path d="M1 3l5 3.6L11 3" fill="none" stroke="var(--card-black)" stroke-width=".8"/></svg>
          hello@harbingernaw.com
        </li>
        <li>
          <svg class="contact-icon" viewBox="0 0 12 12" aria-hidden="true"><circle cx="6" cy="6" r="5.5" fill="var(--gold)"/><path d="M.5 6h11M6 .5c-2 2.8-2 8.2 0 11M6 .5c2 2.8 2 8.2 0 11" fill="none" stroke="var(--card-black)" stroke-width=".7"/></svg>
          www.harbingernaw.com
        </li>
      </ul>
    </div>
    <div class="notes-panel" aria-label="Space for handwritten notes">
      <span class="notes-line"></span>
      <span class="notes-line"></span>
    </div>
  </section>

</body>
</html>
```